New Billboard Design Project

I would like a billboard with the attached image of me Vectored onto it. With my name Marcus Thornley

also the attached logo

Maybe saying "WELCOME TO BRIGHTMEADOW" large across the top.

Real Estate Professional

1.75% FULL listing service

Call/Text 410-937-2815

(Then the text below much smaller because it is required by law)

Office: 833-555-2947
2741 W Harrowgate Rd
Bel Air, MD 21014
www.brightmeadowhomes.com

Billboard size is:

48 FT X 14 FT

```html
<!DOCTYPE html>
<html lang="en">
<head>
<meta charset="utf-8">
<title>Brightmeadow Billboard</title>
<link rel="stylesheet" href="https://fonts.googleapis.com/css2?family=Open+Sans:wght@400;600;700;800&display=swap">
<style>
  :root {
    --navy: #0f2d5c;
    --ink: #1d2f55;
    --text-grey: #3a3f47;
    --rule-grey: #7b7f86;
    --panel-white: #ffffff;
    --page: #c9cbce;
    --photo-top: #e4e1de;
    --photo-mid: #b9a9a0;
    --photo-low: #2a3a60;
    --photo-base: #1b294a;
  }
  * { box-sizing: border-box; margin: 0; padding: 0; }
  html, body { width: 1127px; height: 1200px; overflow: hidden; }
  body {
    background: var(--page);
    font-family: "Open Sans", Arial, sans-serif;
    position: relative;
  }
  .billboard {
    position: absolute;
    left: 30px; top: 445px;
    width: 1067px; height: 310px;
    overflow: hidden;
    box-shadow: 0 6px 18px rgba(0,0,0,.25);
  }
  .billboard-bg { position: absolute; inset: 0; }

  /* Left information column */
  .identity {
    position: absolute;
    left: 62px; top: 0; width: 290px; height: 310px;
    display: flex; flex-direction: column; align-items: center; justify-content: center;
    gap: 0;
    color: var(--navy);
  }
  .brand-kicker {
    display: flex; align-items: center; gap: 12px; width: 100%;
    font-size: 13px; font-weight: 600; letter-spacing: 8px; text-transform: uppercase;
    color: var(--navy);
  }
  .brand-kicker::before, .brand-kicker::after { content: ""; flex: 1; height: 1px; background: var(--navy); }
  .brand {
    display: flex; align-items: center; justify-content: center; gap: 12px;
    margin-top: 6px;
  }
  .brand-mark { width: 20px; height: 20px; border-radius: 50%; background: var(--navy); }
  .brand-name { font-size: 40px; font-weight: 700; line-height: 48px; letter-spacing: .3px; color: var(--navy); }
  .brand-sub {
    display: flex; align-items: center; gap: 10px; width: 100%;
    margin-top: 4px;
    font-size: 11px; font-weight: 600; letter-spacing: 2.4px; text-transform: uppercase;
    white-space: nowrap;
  }
  .brand-sub::before, .brand-sub::after { content: ""; flex: 1; height: 1px; background: var(--navy); }
  .office-details {
    width: 100%; margin-top: 30px;
    text-align: center; color: var(--text-grey);
  }
  .office-phone { color: var(--navy); font-weight: 700; font-size: 13px; line-height: 18px; }
  .office-address { font-size: 13px; line-height: 18px; display: flex; align-items: center; justify-content: center; gap: 4px; white-space: nowrap; }
  .office-rule { height: 1px; background: var(--rule-grey); margin: 4px 0 6px; }
  .office-web { font-size: 13px; display: flex; align-items: center; justify-content: center; gap: 5px; }
  .office-web b { color: var(--navy); }

  /* Agent portrait area */
  .agent-photo {
    position: absolute;
    left: 400px; top: 0; width: 265px; height: 310px;
    background:
      radial-gradient(ellipse 40% 30% at 48% 22%, var(--photo-mid) 0%, rgba(185,169,160,0) 100%),
      linear-gradient(180deg, var(--photo-top) 0%, #cfc8c3 30%, var(--photo-low) 62%, var(--photo-base) 100%);
  }
  .agent-name {
    position: absolute;
    left: 424px; top: 268px; width: 196px; height: 32px;
    background: var(--panel-white);
    border-radius: 16px;
    color: var(--ink);
    font-size: 20px; font-weight: 600;
    display: flex; align-items: center; justify-content: center;
    box-shadow: 0 1px 4px rgba(0,0,0,.3);
  }

  /* Right message column */
  .welcome {
    position: absolute; left: 680px; top: 16px; width: 345px;
    display: flex; align-items: center; gap: 8px;
    color: #fff; font-size: 25px; font-weight: 400; letter-spacing: .5px;
  }
  .welcome::before, .welcome::after { content: ""; flex: 1; height: 2px; background: #fff; }
  .market-name {
    position: absolute; left: 665px; top: 45px; width: 375px;
    text-align: center; color: #fff;
    font-size: 44px; font-weight: 800; letter-spacing: -.5px; line-height: 56px;
  }
  .title-ribbon {
    position: absolute; left: 672px; top: 114px; width: 355px; height: 40px;
    display: flex; align-items: center; justify-content: center;
    color: var(--ink); font-size: 21px; font-weight: 700;
  }
  .offer {
    position: absolute; left: 680px; top: 172px; width: 380px; height: 76px;
    display: flex; align-items: center; gap: 10px; color: #fff;
  }
  .offer-rate { font-size: 62px; font-weight: 800; letter-spacing: -2px; text-shadow: 1px 2px 2px rgba(0,0,0,.35); }
  .offer-label { font-size: 20px; font-weight: 800; line-height: 26px; }
  .call-line {
    position: absolute; left: 665px; top: 258px; width: 375px;
    text-align: center; color: #fff; font-size: 26px; font-weight: 700;
  }
</style>
</head>
<body>
  <section class="billboard">
    <svg class="billboard-bg" width="1067" height="310" viewBox="0 0 1067 310">
      <defs>
        <linearGradient id="panelFade" x1="0" y1="0" x2="1" y2="0">
          <stop offset="0" stop-color="#e3e4e6"/>
          <stop offset=".6" stop-color="#ffffff"/>
        </linearGradient>
        <linearGradient id="bandFade" x1="0" y1="0" x2="1" y2="0">
          <stop offset="0" stop-color="#3a8ee0"/>
          <stop offset=".7" stop-color="#1c5fae"/>
          <stop offset="1" stop-color="#123f80"/>
        </linearGradient>
        <linearGradient id="silver" x1="0" y1="0" x2="0" y2="1">
          <stop offset="0" stop-color="#f2f3f4"/>
          <stop offset=".6" stop-color="#c9ccd0"/>
          <stop offset="1" stop-color="#9ea3a8"/>
        </linearGradient>
      </defs>
      <rect width="1067" height="310" fill="#0f2d5c"/>
      <polygon points="0,0 528,0 430,310 0,310" fill="url(#panelFade)"/>
      <polygon points="650,172 1067,172 1067,248 662,248" fill="url(#bandFade)"/>
      <polygon points="672,114 1027,114 1017,134 1027,154 672,154 682,134" fill="url(#silver)"/>
    </svg>

    <div class="identity">
      <p class="brand-kicker">The</p>
      <div class="brand">
        <span class="brand-mark"></span>
        <span class="brand-name">Harlow Group</span>
      </div>
      <p class="brand-sub">Keystone Realty Partners</p>
      <div class="office-details">
        <p class="office-phone">Office: 833-555-2947</p>
        <p class="office-address">
          <svg width="10" height="12" viewBox="0 0 10 12"><path d="M5 0a4 4 0 0 0-4 4c0 3 4 7 4 7s4-4 4-7a4 4 0 0 0-4-4z" fill="#0f2d5c"/><circle cx="5" cy="4" r="1.5" fill="#fff"/></svg>
          2741 W Harrowgate Rd Bel Air, MD 21014
        </p>
        <div class="office-rule"></div>
        <p class="office-web">
          <svg width="12" height="12" viewBox="0 0 12 12"><circle cx="6" cy="6" r="5.5" fill="#0f2d5c"/><path d="M1 6h10M6 1c-2 2-2 8 0 10M6 1c2 2 2 8 0 10" stroke="#fff" stroke-width=".8" fill="none"/></svg>
          <span>www.<b>brightmeadowhomes</b>.com</span>
        </p>
      </div>
    </div>

    <div class="agent-photo" role="img" aria-label="Vector portrait of Marcus Thornley in a navy suit and light shirt"></div>
    <div class="agent-name">Marcus Thornley</div>

    <p class="welcome">WELCOME TO</p>
    <h1 class="market-name">BRIGHTMEADOW</h1>
    <p class="title-ribbon">REAL ESTATE PROFESSIONAL</p>
    <div class="offer">
      <span class="offer-rate">1.75%</span>
      <span class="offer-label">FULL LISTING<br>SERVICE</span>
    </div>
    <p class="call-line">Call/Text: 410-937-2815</p>
  </section>
</body>
</html>
```